Business Card Design Project

Hi,
This is a simple contest. The logo for the back of the card is deigned. See attached files. The front of the card must have :

Directors Name: Tobias
Mob:
e-mail:
Postal Address:
Web Page Adress:

It may also add words: "Leaders in Construction Project Management Services"

Target Market(s)

Business & Home owners alike

Industry/Entity Type

Business

Requirements
Must have
• See details above and logo attached
Should not have
• Images other than logo

```html
<!DOCTYPE html>
<html lang="en">
<head>
<meta charset="utf-8">
<title>Keystone Build Partners – Business Card</title>
<link rel="stylesheet" href="https://fonts.googleapis.com/css2?family=Source+Sans+3:wght@400;600;700&display=swap">
<style>
  :root {
    --brand-blue: #0a9bdc;
    --brand-blue-deep: #0888c4;
    --ink: #1d1d1f;
    --paper: #ffffff;
    --stage: #2a2a2c;
    --font: "Source Sans 3", "Helvetica Neue", Arial, sans-serif;
  }
  * { box-sizing: border-box; margin: 0; padding: 0; }
  html, body {
    width: 1200px; height: 900px; overflow: hidden;
    background: var(--stage);
    font-family: var(--font);
  }
  .sheet {
    width: 1200px; height: 900px;
    display: flex; flex-direction: column;
    align-items: center; justify-content: center; gap: 40px;
  }
  .card {
    position: relative;
    width: 640px; height: 366px;
    overflow: hidden;
  }

  /* Back side */
  .card--back {
    background: var(--brand-blue);
    color: var(--paper);
  }
  .card--back .brand {
    position: absolute; left: 88px; top: 128px;
    display: flex; align-items: center; gap: 18px;
  }
  .brand__square {
    width: 62px; height: 62px;
    background: currentColor;
  }
  .brand__name {
    font-weight: 700; font-size: 38px; line-height: 1;
    letter-spacing: 0.5px;
  }
  .card--back .tagline {
    position: absolute; left: 168px; top: 206px;
    font-size: 15px; font-weight: 400; letter-spacing: 0.2px;
  }

  /* Front side */
  .card--front {
    background: var(--paper);
    color: var(--ink);
  }
  .card--front .brand {
    position: absolute; left: 44px; top: 52px;
    display: flex; align-items: center; gap: 16px;
    color: var(--brand-blue);
  }
  .card--front .brand__square { width: 50px; height: 50px; }
  .card--front .brand__name { font-size: 31px; }

  .contact {
    position: absolute; left: 140px; top: 170px;
  }
  .contact__name {
    color: var(--brand-blue);
    font-size: 25px; font-weight: 400; line-height: 1.1;
  }
  .contact__role {
    font-size: 16px; font-weight: 400; letter-spacing: 0.3px;
    text-transform: uppercase; margin-top: 2px;
  }
  .contact__list {
    list-style: none; margin-top: 18px;
    font-size: 18px;
  }
  .contact__list li {
    display: flex; align-items: center; gap: 10px; height: 28px;
  }
  .contact__list svg { width: 16px; height: 16px; flex: none; }

  .address {
    position: absolute; left: 420px; top: 218px;
    padding-left: 14px;
    border-left: 2px solid var(--brand-blue);
    font-size: 17px; line-height: 1.45;
  }

  .card__band {
    position: absolute; left: 0; right: 0; bottom: 0;
    height: 30px;
    background: var(--brand-blue-deep);
  }
</style>
</head>
<body>
<main class="sheet">

  <section class="card card--back" aria-label="Card back">
    <div class="brand">
      <span class="brand__square"></span>
      <span class="brand__name">KEYSTONE BUILD PARTNERS</span>
    </div>
    <p class="tagline">Construction Project Management Services</p>
  </section>

  <section class="card card--front" aria-label="Card front">
    <div class="brand">
      <span class="brand__square"></span>
      <span class="brand__name">KEYSTONE BUILD PARTNERS</span>
    </div>

    <div class="contact">
      <p class="contact__name">Angelo Tobias</p>
      <p class="contact__role">Managing Director</p>
      <ul class="contact__list">
        <li>
          <svg viewBox="0 0 16 16" aria-hidden="true">
            <rect x="4" y="1" width="8" height="14" rx="1.5" fill="none" stroke="#0a9bdc" stroke-width="1.6"/>
            <circle cx="8" cy="12.3" r="0.9" fill="#0a9bdc"/>
          </svg>
          <span>0400 555 217</span>
        </li>
        <li>
          <svg viewBox="0 0 16 16" aria-hidden="true">
            <circle cx="8" cy="8" r="6.6" fill="none" stroke="#0a9bdc" stroke-width="1.4"/>
            <ellipse cx="8" cy="8" rx="2.8" ry="6.6" fill="none" stroke="#0a9bdc" stroke-width="1.2"/>
            <line x1="1.4" y1="8" x2="14.6" y2="8" stroke="#0a9bdc" stroke-width="1.2"/>
          </svg>
          <span>www.keystone-bp.com.au</span>
        </li>
      </ul>
    </div>

    <address class="address" style="font-style: normal;">
      48 Harbour Lane<br>
      Brookvale, NSW 2100
    </address>

    <div class="card__band"></div>
  </section>

</main>
</body>
</html>
```